Design few pages for professional development app

I need a website design for a prototype project. The goal of the project is to prototype a few basic screens for a professional development application.

The final design should be clean, modern, and appeal to a professional millenial clientele.The designs have been wireframed (see attached), and we'd like these wireframes converted to design files.

Here is the list of goals and tasks that correspond to the design: https://sheets.plorvane.com/grid/d/7kQWm48p3XZvrt2bYH5LcNaeJoTsUDfi82GhKxMp/edit?view=shared

Number of Pages Required

5+ page

Font styles to use
Serif
Sans Serif

Colors

Designer to choose colors to be used in the design.

Requirements
Nice to have
• Uses Google Material Design, Bootstrap, or another framework

```html
<!DOCTYPE html>
<html lang="en">
<head>
<meta charset="utf-8">
<title>Climbwell – Take Control of Your Career</title>
<link rel="stylesheet" href="https://fonts.googleapis.com/css2?family=Nunito:ital,wght@0,400;0,600;0,700;0,800;1,400&display=swap">
<style>
  :root {
    --page-bg: #eaeff4;
    --header-bg: #ffffff;
    --ink: #3d4b5c;
    --brand-blue: #1a6dc4;
    --hero-yellow: #eeb524;
    --hero-yellow-deep: #e6ab1e;
    --hero-yellow-light: #fdd663;
    --figure-tone: rgba(150, 110, 50, 0.35);
    --white: #ffffff;
    --search-bg: #d9e0e8;
    --search-icon: #6b7886;
    --card-teal: #acd9e0;
    --quote-teal: #1f97a8;
    --card-peach: #efd3b6;
    --quote-orange: #ef7d1a;
  }
  * { box-sizing: border-box; margin: 0; padding: 0; }
  html, body {
    width: 1200px; height: 675px; overflow: hidden;
    background: var(--page-bg);
    font-family: "Nunito", sans-serif;
    color: var(--ink);
  }
  .site-header {
    position: absolute; left: 0; top: 0; width: 1200px; height: 50px;
    background: var(--header-bg);
  }
  .brand {
    position: absolute; left: 24px; top: 14px;
    font-size: 15px; font-weight: 800; color: var(--brand-blue);
  }
  .search-button {
    position: absolute; left: 1145px; top: 10px; width: 30px; height: 30px;
    border-radius: 5px; background: var(--search-bg);
    display: flex; align-items: center; justify-content: center;
  }
  .hero {
    position: absolute; left: 252px; top: 100px; width: 694px; height: 295px;
    border-radius: 10px; overflow: hidden;
  }
  .hero-photo {
    position: absolute; inset: 0;
    background:
      radial-gradient(ellipse 110px 150px at 545px 150px, var(--figure-tone), transparent 75%),
      linear-gradient(160deg, var(--hero-yellow) 0%, var(--hero-yellow-deep) 55%, var(--hero-yellow-light) 100%);
  }
  .hero-title {
    position: absolute; left: 0; right: 0; top: 60px;
    text-align: center; color: var(--white);
    font-size: 35px; font-weight: 800; line-height: 42px;
  }
  .hero-text {
    position: absolute; left: 131px; width: 432px; top: 119px;
    text-align: center; color: var(--white);
    font-size: 11.2px; font-weight: 600; line-height: 17px;
  }
  .cta-button {
    position: absolute; left: 288px; top: 192px; width: 120px; height: 36px;
    border-radius: 5px; background: var(--brand-blue); color: var(--white);
    font-size: 12.5px; font-weight: 700;
    display: flex; align-items: center; justify-content: center;
    box-shadow: 0 4px 10px rgba(20, 60, 120, 0.3);
  }
  .testimonial {
    position: absolute; top: 468px; width: 224px; height: 94px;
    border-radius: 8px; padding: 17px 20px 0 47px;
  }
  .testimonial--teal { left: 341px; background: var(--card-teal); }
  .testimonial--peach { left: 637px; background: var(--card-peach); }
  .avatar {
    position: absolute; top: 19px; left: -28px; width: 56px; height: 56px;
    border-radius: 6px; box-shadow: 0 6px 14px rgba(0, 0, 0, 0.2);
  }
  .testimonial--teal .avatar { background: linear-gradient(135deg, #c9713a, #8a4a2c); }
  .testimonial--peach .avatar { background: linear-gradient(135deg, #3f5b66, #25363d); }
  .quote-text {
    font-size: 11.2px; font-style: italic; line-height: 17px;
  }
  .quote-author {
    margin-top: 4px; font-size: 11.2px; font-weight: 700;
  }
  .quote-mark {
    position: absolute; right: 14px; top: 62px;
    font-size: 40px; font-weight: 800; line-height: 0.8;
  }
  .testimonial--teal .quote-mark { color: var(--quote-teal); }
  .testimonial--peach .quote-mark { color: var(--quote-orange); }
</style>
</head>
<body>
  <header class="site-header">
    <div class="brand">Climbwell</div>
    <div class="search-button" aria-label="Search">
      <svg width="16" height="16" viewBox="0 0 24 24">
        <circle cx="10" cy="10" r="6.5" fill="none" stroke="var(--search-icon)" stroke-width="2.5"/>
        <line x1="15" y1="15" x2="21" y2="21" stroke="var(--search-icon)" stroke-width="3" stroke-linecap="round"/>
      </svg>
    </div>
  </header>

  <section class="hero">
    <div class="hero-photo" role="img" aria-label="Photo of a woman leaping with an umbrella in front of a yellow wooden wall, with a decorative blue corner and a light yellow wave"></div>
    <h1 class="hero-title">Take Control of Your Career</h1>
    <p class="hero-text">Complete short, actionable tasks guaranteed to get you further in your career, faster than ever. Ready to get started? Take the short quiz below and get your personalized path today.</p>
    <div class="cta-button">Get Started</div>
  </section>

  <article class="testimonial testimonial--teal">
    <div class="avatar" role="img" aria-label="Portrait of Nora Ellis"></div>
    <p class="quote-text">I love how quickly I can do the tasks, and see progress.</p>
    <p class="quote-author">Nora Ellis</p>
    <span class="quote-mark">&ldquo;</span>
  </article>

  <article class="testimonial testimonial--peach">
    <div class="avatar" role="img" aria-label="Portrait of Theo Marsh"></div>
    <p class="quote-text">The best investment I’ve made in myself in ages.</p>
    <p class="quote-author">Theo Marsh</p>
    <span class="quote-mark">&ldquo;</span>
  </article>
</body>
</html>
```